Business Card Design Project

- makeup artist business card

- original and creative

- Elegant design

- Feel free to come out with cool designs but stick to being elegant and attractive

- Design relates to makeup

- includes name, occupation, contact numbers, email, website

- regular size business card

- round corner card

- double sided

- on 1 side it should just have the website name in the center " browsandblush.example "

Industry/Entity Type

Business

Requirements
Must have
• Marla Voss
Makeup Artist
USA: +1 (415)872-6410
Singapore: +65 83027715
marlavoss@browsandblush.example
www.browsandblush.example
Should not have
• nothing cartoon looking.
Pictures of makeup being grab from the internet.. Examples: eyes or lips.

```html
<!DOCTYPE html>
<html lang="en">
<head>
<meta charset="utf-8">
<title>Marla Voss – Makeup Artist Business Card</title>
<link rel="stylesheet" href="https://fonts.googleapis.com/css2?family=Tinos:wght@400;700&display=swap">
<style>
  :root {
    --page-bg: #e9e7e5;
    --card-base: #3a2a27;
    --card-edge: #2a1e1c;
    --glow-red: rgba(190, 30, 20, 0.55);
    --bar-red: #d41a1a;
    --bar-red-dark: #8e0d0d;
    --bar-red-light: #ff3a30;
    --text-white: #ffffff;
    --text-red: #e8231c;
  }
  * { margin: 0; padding: 0; box-sizing: border-box; }
  html, body {
    width: 1068px;
    height: 1200px;
    overflow: hidden;
    background: var(--page-bg);
  }
  .sheet {
    position: relative;
    width: 1068px;
    height: 1200px;
    display: flex;
    flex-direction: column;
    align-items: center;
    justify-content: center;
    gap: 60px;
    font-family: "Tinos", "Times New Roman", serif;
  }
  .card {
    position: relative;
    width: 900px;
    height: 520px;
    border-radius: 40px;
    overflow: hidden;
    background:
      radial-gradient(ellipse at 50% 50%, #4a3430 0%, var(--card-base) 55%, var(--card-edge) 100%);
    box-shadow: 0 10px 30px rgba(0, 0, 0, 0.25);
  }
  .card__ornament {
    position: absolute;
    inset: 0;
    background:
      radial-gradient(circle at 46% 42%, var(--glow-red) 0%, rgba(150, 25, 18, 0.25) 18%, transparent 38%),
      radial-gradient(ellipse at 72% 70%, rgba(30, 18, 16, 0.45) 0%, transparent 30%),
      radial-gradient(ellipse at 20% 55%, rgba(80, 55, 48, 0.35) 0%, transparent 35%);
  }
  .card__bar {
    position: absolute;
    left: 22px;
    right: 22px;
    height: 16px;
    background: linear-gradient(90deg, var(--bar-red-dark) 0%, var(--bar-red) 30%, var(--bar-red-light) 55%, var(--bar-red) 80%, var(--bar-red-dark) 100%);
    box-shadow: inset 0 -2px 0 rgba(0, 0, 0, 0.25), inset 0 2px 0 rgba(255, 120, 110, 0.35);
  }
  .card__bar--top { top: 40px; }
  .card__bar--bottom { bottom: 40px; }

  .identity {
    position: absolute;
    left: 80px;
    top: 182px;
    text-align: right;
  }
  .identity__name {
    font-size: 48px;
    font-weight: 700;
    line-height: 1;
    color: var(--text-white);
    text-shadow: 0 2px 3px rgba(0, 0, 0, 0.5);
  }
  .identity__surname { color: var(--text-red); }
  .identity__role {
    margin-top: 10px;
    font-size: 26px;
    color: var(--text-white);
  }

  .contact {
    position: absolute;
    left: 416px;
    top: 186px;
    font-size: 23px;
    line-height: 29px;
    list-style: none;
  }
  .contact__item { color: var(--text-white); }
  .contact__item--link { color: var(--text-red); }

  .card__website {
    position: absolute;
    left: 0;
    right: 0;
    top: 50%;
    transform: translateY(-50%);
    text-align: center;
    font-size: 46px;
    color: var(--text-white);
    text-shadow: 0 2px 3px rgba(0, 0, 0, 0.5);
  }
</style>
</head>
<body>
  <main class="sheet">
    <section class="card card--front" aria-label="Business card front">
      <div class="card__ornament" role="img" aria-label="Floral swirl ornament with a soft red glow on a dark brown ground"></div>
      <div class="card__bar card__bar--top"></div>
      <div class="identity">
        <h1 class="identity__name">Marla <span class="identity__surname">Voss</span></h1>
        <p class="identity__role">Makeup Artist</p>
      </div>
      <ul class="contact">
        <li class="contact__item">Phone USA: +1 (415)872-6410</li>
        <li class="contact__item">Singapore: +65 83027715: 0427 318 592</li>
        <li class="contact__item contact__item--link">marlavoss@browsandblush.example</li>
        <li class="contact__item contact__item--link">www.browsandblush.example</li>
      </ul>
      <div class="card__bar card__bar--bottom"></div>
    </section>

    <section class="card card--back" aria-label="Business card back">
      <div class="card__ornament" role="img" aria-label="Floral swirl ornament with a soft red glow on a dark brown ground"></div>
      <div class="card__bar card__bar--top"></div>
      <p class="card__website">www.browsandblush.example</p>
      <div class="card__bar card__bar--bottom"></div>
    </section>
  </main>
</body>
</html>
```